New Business Card Design Project

Use the flyer uploaded and website www.brightoakbuilders.com for inspiration.
List Our Services on Backside of business cards
Martin Hollis
Harborline Renovations Inc.
Licensed General Contractors
858-471-9063

Contact Information for Business Card

Use the flyer uploaded and website www.brightoakbuilders.com for inspiration. List Our Services on Backside of business cards Martin Hollis Harborline Renovations Inc. Licensed General Contractors 858-471-9063

```html
<!DOCTYPE html>
<html lang="en">
<head>
<meta charset="utf-8">
<title>Harborline Renovations – Business Card</title>
<link href="https://fonts.googleapis.com/css2?family=Marcellus&family=Cinzel:wght@700&family=Arimo:wght@400&display=swap" rel="stylesheet">
<style>
  :root {
    --page-bg: #1c1c1c;
    --card-light: #ffffff;
    --card-dark: #2f2f2f;
    --ink-dark: #1d1d1d;
    --ink-muted: #6b6b6b;
    --ink-light: #f4f4f4;
    --rule-light: #9a9a9a;
    --rule-dark: #8a8a8a;
  }
  * { margin: 0; padding: 0; box-sizing: border-box; }
  html, body { width: 1200px; height: 963px; overflow: hidden; }
  body {
    background: var(--page-bg);
    position: relative;
    font-family: "Arimo", Arial, sans-serif;
  }
  .card {
    position: absolute;
    left: 250px;
    width: 700px;
    height: 400px;
    border-radius: 26px;
    overflow: hidden;
  }
  .card--front { top: 41px; background: var(--card-light); }
  .card--back { top: 522px; background: var(--card-dark); }

  .wordmark {
    position: absolute;
    left: 40px;
    top: 150px;
    width: 270px;
    display: flex;
    align-items: center;
    gap: 12px;
    font-family: "Marcellus", serif;
    font-size: 27px;
    line-height: 1.15;
    letter-spacing: 1px;
    text-transform: uppercase;
  }
  .wordmark__dot {
    flex: none;
    width: 14px; height: 14px;
    border-radius: 50%;
  }
  .card--front .wordmark { color: var(--ink-dark); }
  .card--front .wordmark__dot { background: var(--ink-dark); }
  .card--back .wordmark { color: var(--ink-light); top: 80px; }
  .card--back .wordmark__dot { background: var(--ink-light); }

  .divider {
    position: absolute;
    left: 335px;
    width: 1px;
  }
  .card--front .divider { top: 120px; height: 160px; background: var(--rule-light); }
  .card--back .divider { top: 40px; height: 240px; background: var(--rule-dark); }

  .contact { position: absolute; left: 370px; top: 120px; }
  .contact__name {
    font-family: "Cinzel", serif;
    font-weight: 700;
    font-size: 30px;
    color: var(--ink-dark);
    letter-spacing: 1px;
  }
  .contact__role { font-size: 20px; color: var(--ink-muted); margin-top: 2px; }
  .contact__list { list-style: none; margin-top: 26px; }
  .contact__item {
    display: flex; align-items: center; gap: 12px;
    font-size: 20px; color: var(--ink-muted); margin-bottom: 8px;
  }
  .contact__item svg { width: 18px; height: 18px; flex: none; }

  .wave { position: absolute; left: 0; bottom: 0; width: 700px; height: 140px; }

  .services { position: absolute; left: 365px; top: 36px; color: var(--ink-light); }
  .services__title {
    font-family: "Marcellus", serif;
    font-size: 30px;
    letter-spacing: 1px;
    margin-bottom: 8px;
  }
  .services__list { list-style: none; }
  .services__item {
    display: flex; align-items: center; gap: 8px;
    font-size: 17px; line-height: 26px;
  }
  .services__item svg { width: 15px; height: 15px; flex: none; }
</style>
</head>
<body>

<section class="card card--front" aria-label="Business card front">
  <div class="wordmark"><span class="wordmark__dot"></span><span>Harborline Renovations</span></div>
  <div class="divider"></div>
  <div class="contact">
    <h1 class="contact__name">Martin Hollis</h1>
    <p class="contact__role">Licensed General Contractors</p>
    <ul class="contact__list">
      <li class="contact__item">
        <svg viewBox="0 0 24 24" fill="none" stroke="#1d1d1d" stroke-width="2.2" stroke-linecap="round" stroke-linejoin="round"><path d="M5 3h4l2 5-2.5 1.5a11 11 0 0 0 6 6L16 13l5 2v4a2 2 0 0 1-2 2A17 17 0 0 1 3 5a2 2 0 0 1 2-2z"/></svg>
        858-471-9063
      </li>
      <li class="contact__item">
        <svg viewBox="0 0 24 24" fill="none" stroke="#1d1d1d" stroke-width="2"><circle cx="12" cy="12" r="10"/><path d="M2 12h20M12 2a15 15 0 0 1 0 20M12 2a15 15 0 0 0 0 20"/></svg>
        www.brightoakbuilders.com
      </li>
    </ul>
  </div>
  <svg class="wave" viewBox="0 0 700 140" preserveAspectRatio="none" aria-hidden="true">
    <path d="M0 20 C 120 30, 200 90, 330 130 L 330 140 L 0 140 Z" fill="#2a2a2a"/>
    <path d="M0 8 C 130 14, 210 80, 330 122" fill="none" stroke="#2a2a2a" stroke-width="4"/>
    <path d="M700 140 L 700 118 C 560 120, 450 90, 300 140 Z" fill="#2a2a2a"/>
    <path d="M700 106 C 560 108, 450 78, 310 128" fill="none" stroke="#2a2a2a" stroke-width="3"/>
  </svg>
</section>

<section class="card card--back" aria-label="Business card back">
  <div class="wordmark"><span class="wordmark__dot"></span><span>Harborline Renovations</span></div>
  <div class="divider"></div>
  <div class="services">
    <h2 class="services__title">OUR SERVICES</h2>
    <ul class="services__list">
      <li class="services__item"><svg viewBox="0 0 24 24" fill="none" stroke="#f4f4f4" stroke-width="2.6"><circle cx="12" cy="12" r="10"/><path d="M7 12l3.5 3.5L17 9"/></svg>Remodel: Kitchen &amp; Bath</li>
      <li class="services__item"><svg viewBox="0 0 24 24" fill="none" stroke="#f4f4f4" stroke-width="2.6"><circle cx="12" cy="12" r="10"/><path d="M7 12l3.5 3.5L17 9"/></svg>Painting: Interior &amp; Exterior</li>
      <li class="services__item"><svg viewBox="0 0 24 24" fill="none" stroke="#f4f4f4" stroke-width="2.6"><circle cx="12" cy="12" r="10"/><path d="M7 12l3.5 3.5L17 9"/></svg>Flooring: Carpet, Vinyl, Wood</li>
      <li class="services__item"><svg viewBox="0 0 24 24" fill="none" stroke="#f4f4f4" stroke-width="2.6"><circle cx="12" cy="12" r="10"/><path d="M7 12l3.5 3.5L17 9"/></svg>Window &amp; Door Replacement</li>
      <li class="services__item"><svg viewBox="0 0 24 24" fill="none" stroke="#f4f4f4" stroke-width="2.6"><circle cx="12" cy="12" r="10"/><path d="M7 12l3.5 3.5L17 9"/></svg>Plumbing: Repairs &amp; Upgrades</li>
      <li class="services__item"><svg viewBox="0 0 24 24" fill="none" stroke="#f4f4f4" stroke-width="2.6"><circle cx="12" cy="12" r="10"/><path d="M7 12l3.5 3.5L17 9"/></svg>Energy-Efficient Upgrades</li>
      <li class="services__item"><svg viewBox="0 0 24 24" fill="none" stroke="#f4f4f4" stroke-width="2.6"><circle cx="12" cy="12" r="10"/><path d="M7 12l3.5 3.5L17 9"/></svg>Deck &amp; Patio Construction</li>
      <li class="services__item"><svg viewBox="0 0 24 24" fill="none" stroke="#f4f4f4" stroke-width="2.6"><circle cx="12" cy="12" r="10"/><path d="M7 12l3.5 3.5L17 9"/></svg>Water &amp; Mold Damage</li>
      <li class="services__item"><svg viewBox="0 0 24 24" fill="none" stroke="#f4f4f4" stroke-width="2.6"><circle cx="12" cy="12" r="10"/><path d="M7 12l3.5 3.5L17 9"/></svg>Garage Renovation</li>
    </ul>
  </div>
</section>

</body>
</html>
```